Tamrick Holdings envision a corporate 22 year old theme with as many features functional

We need an interactive website designed.
Fully interactive with social media
Fully Interactive with Live content
you should map out how you'd like the website to work. This is important both for user experience and for SEO, since Wexlo considers the content and structure of a site when it ranks
Crucial Business Information
Keep text to a minimum when it comes to your mission statement, because you should be writing things so people can skim — we all have short attention spans.
Depending on your business, you should have a few things on your website that fall into the realm of "information." Tailor your site so that it offers the information users are likely to be looking for.
Content
Clear Navigation
Security
Social Media Intergration
Mobile Ready
Feel free to forgo these things on your website:
Music
Flash
Anything that autoplays,
Extraneous information and media
Media
Coded - Design and coding required
1 page
- as per uploaded Guidelines

```html
<!DOCTYPE html>
<html lang="en">
<head>
<meta charset="utf-8">
<title>Tamrick Holdings — people capital strategy</title>
<link rel="stylesheet" href="https://fonts.googleapis.com/css2?family=Titillium+Web:wght@400;600;700&family=Open+Sans:wght@400;600;700&display=swap">
<style>
:root{
  --green:#2bb583;
  --green-dark:#1f9a6e;
  --ink:#1f1f1f;
  --night:#232323;
  --text:#4a4a4a;
  --mist:#f1f1f1;
  --field:#ececec;
  --frame:#e6e6e6;
  --white:#ffffff;
}
*{margin:0;padding:0;box-sizing:border-box}
html,body{width:1200px;height:3072px;overflow:hidden}
body{background:var(--frame);font-family:"Open Sans",Arial,sans-serif;color:var(--text)}
.page{position:absolute;left:14px;top:14px;width:1172px;height:3044px;background:var(--white);box-shadow:0 0 6px rgba(0,0,0,.18);overflow:hidden}
.display{font-family:"Titillium Web","Open Sans",sans-serif}

/* header */
.site-header{position:absolute;left:0;top:0;width:1172px;height:112px;background:var(--night)}
.brand{position:absolute;left:30px;top:38px;display:flex;align-items:center;gap:10px;font-family:"Titillium Web",sans-serif;font-weight:700;font-size:26px;color:var(--white)}
.brand-dot{width:16px;height:16px;border-radius:50%;background:var(--green)}
.main-nav{position:absolute;right:22px;top:62px;display:flex;gap:20px;font-family:"Open Sans",sans-serif;font-size:13px;font-weight:600;color:#e4e4e4;text-transform:uppercase}
.main-nav .is-active{color:var(--green);position:relative}
.main-nav .is-active::before{content:"";position:absolute;left:6px;top:-22px;width:10px;height:10px;border:3px solid var(--green);border-radius:50%}

/* hero */
.hero{position:absolute;left:0;top:112px;width:1172px;height:554px;
  background:
   linear-gradient(180deg,rgba(0,0,0,0) 55%,#0d2a22 58%,#0f3a2e 61%,#1f7e60 70%,#136049 100%),
   radial-gradient(ellipse 70% 25% at 45% 28%,#4ff0b0 0%,rgba(60,220,150,.6) 45%,rgba(0,0,0,0) 100%),
   linear-gradient(180deg,#0b2d3a 0%,#124e48 40%,#1c7a5e 55%);}
.hero-tagline{position:absolute;left:0;right:0;top:250px;text-align:center;font-family:"Titillium Web",sans-serif;font-size:54px;color:var(--white);letter-spacing:.5px}
.sep{display:inline-block;width:14px;height:14px;border:3px solid var(--green);border-radius:50%;margin:0 10px;vertical-align:middle}

/* section titles */
.section-title{position:absolute;left:0;right:0;display:flex;justify-content:center;align-items:center;gap:18px;font-family:"Titillium Web",sans-serif;font-weight:600;font-size:30px;color:var(--ink)}
.section-title::before,.section-title::after{content:"";width:62px;height:1px;background:#cfcfcf}
.section-title .accent{color:var(--green)}
.title-mark{position:relative;width:22px;height:22px;border:4px solid var(--green);border-radius:50%;margin-right:-8px;margin-top:10px}
.title-mark::before{content:"";position:absolute;left:-10px;top:-14px;width:6px;height:6px;border-radius:50%;background:var(--green)}

/* who we are */
.who{position:absolute;left:0;top:666px;width:1172px;height:573px;background:var(--white)}
.who .section-title{top:50px}
.who-grid{position:absolute;left:40px;top:128px;width:1092px;display:flex}
.who-card{flex:1;padding:0 16px;position:relative}
.who-card+.who-card{border-left:1px solid #dedede}
.tab{width:190px;height:40px;margin:0 auto 20px;border-radius:5px;background:var(--green);color:var(--white);font-weight:700;font-size:15px;display:flex;align-items:center;justify-content:center;box-shadow:0 6px 6px -4px rgba(0,0,0,.3)}
.photo{height:186px;width:300px}
.photo.steel{background:linear-gradient(180deg,#f4f4f4,#c9ccd2 60%,#8aa6c8)}
.photo.stairs{background:linear-gradient(135deg,#eef3f7,#9ec9e6 55%,#f0b72b 75%,#dcdcdc)}
.photo.chalk{background:radial-gradient(circle at 55% 45%,#5d7e62,#2d4b36 70%)}
.who-card h3{font-size:20px;font-weight:700;color:var(--ink);margin:24px 0 12px}
.who-card p{font-size:14px;line-height:20px;color:#555;width:310px}

/* what we do */
.what{position:absolute;left:0;top:1239px;width:1172px;height:539px;background:var(--mist)}
.what .section-title{top:48px}
.what-grid{position:absolute;left:40px;top:124px;width:1092px;display:flex}
.what-col{flex:1;padding:0 16px 14px}
.what-col+.what-col{border-left:1px solid #d6d6d6}
.what-col h3{font-size:17px;font-weight:600;color:var(--ink);margin-bottom:16px}
.what-col h3 span{color:var(--green)}
.points{list-style:none}
.points li{position:relative;padding-left:30px;font-size:13.5px;line-height:20px;color:#555;margin-bottom:14px}
.points li::before{content:"";position:absolute;left:4px;top:8px;width:10px;height:10px;border:3px solid var(--green);border-radius:50%}
.points li::after{content:"";position:absolute;left:0;top:0;width:4px;height:4px;border-radius:50%;background:var(--green)}
.btn{position:absolute;left:491px;top:443px;width:190px;height:40px;border-radius:5px;background:var(--green);color:var(--white);font-weight:700;font-size:15px;display:flex;align-items:center;justify-content:center;box-shadow:0 6px 6px -4px rgba(0,0,0,.3)}

/* different */
.different{position:absolute;left:0;top:1778px;width:1172px;height:506px;
  background:
   linear-gradient(180deg,rgba(70,200,150,.75),rgba(30,160,120,.85)),
   linear-gradient(90deg,#3d5e55,#8fbfae 50%,#3d5e55)}
.different .section-title{top:52px;color:var(--white)}
.different .section-title::before,.different .section-title::after{background:rgba(255,255,255,.8)}
.different .title-mark{border-color:var(--white)}
.different .title-mark::before{background:var(--white)}
.diagram{position:absolute;left:0;top:0}
.value{position:absolute;color:var(--white);font-size:13px;font-weight:600;line-height:18px;text-shadow:0 1px 2px rgba(0,0,0,.25)}
.value b{font-family:"Titillium Web",sans-serif;font-size:17px;font-weight:700}
.value.left{text-align:right;width:300px}
.center-name{position:absolute;left:494px;top:252px;width:184px;text-align:center;font-family:"Titillium Web",sans-serif;font-weight:700;font-size:24px;line-height:26px;color:var(--white)}

/* message */
.message{position:absolute;left:0;top:2284px;width:1172px;height:385px;background:var(--white)}
.message .section-title{top:50px}
.field{position:absolute;background:var(--field);font-size:14px;color:#555;padding:12px 14px}
.send{position:absolute;left:594px;top:257px;width:123px;height:46px;background:var(--ink);color:var(--white);font-weight:700;font-size:15px;display:flex;align-items:center;justify-content:center}

/* footer */
.site-footer{position:absolute;left:0;top:2669px;width:1172px;height:344px;background:var(--night)}
.footer-tab{position:absolute;left:416px;top:-36px;width:340px;height:60px;background:var(--night);border-radius:40px 40px 0 0}
.footer-brand{position:absolute;left:0;right:0;top:38px;display:flex;justify-content:center;align-items:center;gap:10px;font-family:"Titillium Web",sans-serif;font-weight:700;font-size:30px;color:var(--white)}
.footer-tagline{position:absolute;left:0;right:0;top:160px;text-align:center;font-family:"Titillium Web",sans-serif;font-size:32px;color:var(--white)}
.footer-tagline .sep{width:10px;height:10px;border-width:2px;margin:0 6px}
.footer-nav{position:absolute;left:0;right:0;top:280px;display:flex;justify-content:center;gap:22px;font-size:13px;font-weight:600;color:#d9d9d9;text-transform:uppercase}
.footer-nav .is-active{color:var(--green)}
.copyright{position:absolute;left:0;top:3013px;width:1172px;height:31px;display:flex;align-items:center;justify-content:center;font-size:9px;font-weight:600;color:#444;text-transform:uppercase}
</style>
</head>
<body>
<div class="page">

  <header class="site-header">
    <div class="brand"><span class="brand-dot"></span>Tamrick Holdings</div>
    <nav class="main-nav">
      <span class="is-active">Home</span><span>Who We Are</span><span>What We Do</span><span>What Makes Us Different</span><span>Contact</span>
    </nav>
  </header>

  <section class="hero" role="img" aria-label="Northern lights glowing green over a forest lake at night">
    <p class="hero-tagline">people<span class="sep"></span>capital<span class="sep"></span>strategy</p>
  </section>

  <section class="who">
    <h2 class="section-title"><span class="title-mark"></span><span>Who <span class="accent">We Are</span></span></h2>
    <div class="who-grid">
      <article class="who-card">
        <div class="tab">Direct</div>
        <div class="photo steel" role="img" aria-label="Silver spheres in a V formation led by a blue sphere"></div>
        <h3>Leading Directors</h3>
        <p>We identify and connect appropriate resources to the relevant opportunity points to create business momentum.</p>
      </article>
      <article class="who-card">
        <div class="tab">Human</div>
        <div class="photo stairs" role="img" aria-label="Golden figure running ahead up a staircase of grey figures"></div>
        <h3>Leading Motivators</h3>
        <p>We generate inspiration, motivation and activation through our shared passion for success and converting opportunity to results.</p>
      </article>
      <article class="who-card">
        <div class="tab">Energy</div>
        <div class="photo chalk" role="img" aria-label="Light bulbs sketched in chalk on a green board"></div>
        <h3>Leading Energisers</h3>
        <p>Together, our collective combination of business capabilities forge a powerful, visible impact – delivered with efficiency and effectiveness.</p>
      </article>
    </div>
  </section>

  <section class="what">
    <h2 class="section-title"><span class="title-mark"></span><span>What <span class="accent">We Do</span></span></h2>
    <div class="what-grid">
      <div class="what-col">
        <h3>We Build <span>Ventures</span></h3>
        <ul class="points">
          <li>We invest people and financial capital in ventures that have potential.</li>
          <li>We create joint ventures with partners that will bring synergies to our house of brands.</li>
          <li>We confidently venture into new markets, industries and initiatives with entrepreneurial energy.</li>
        </ul>
      </div>
      <div class="what-col">
        <h3>We are <span>Energising Opportunities</span></h3>
        <ul class="points">
          <li>Our passion for business, performance and success energises our ventures, our people, and the opportunities we invest in.</li>
          <li>Our vision and focus energises people to see beyond what is, to what could be, oppening up new opportunities.</li>
          <li>The opportunities we create energise existing ventures with positive momentum.</li>
        </ul>
      </div>
      <div class="what-col">
        <h3>We Deliver <span>People</span></h3>
        <ul class="points">
          <li>We invest in our people supporting their personal and professional growth.</li>
          <li>We invest our people and financial capital into partnerships driving success.</li>
          <li>We provide the strategic leadership, direction and vision with a strategy of empowering our ventures.</li>
        </ul>
      </div>
    </div>
    <div class="btn">Learn More</div>
  </section>

  <section class="different" role="group" aria-label="City skyline at dusk tinted green, behind the values diagram">
    <h2 class="section-title"><span class="title-mark"></span><span>What Makes Us Different</span></h2>
    <svg class="diagram" width="1172" height="506" viewBox="0 0 1172 506" aria-hidden="true">
      <g stroke="#ffffff" stroke-width="2" fill="none" opacity=".8">
        <path d="M437 178 L480 178 L520 222"/>
        <path d="M735 178 L692 178 L652 222"/>
        <path d="M437 373 L480 373 L520 330"/>
        <path d="M735 373 L692 373 L652 330"/>
      </g>
      <circle cx="586" cy="276" r="94" fill="#1f1f1f" stroke="#ffffff" stroke-width="6"/>
      <g fill="#1f1f1f" stroke="#ffffff" stroke-width="4">
        <circle cx="396" cy="178" r="41"/>
        <circle cx="776" cy="178" r="41"/>
        <circle cx="396" cy="373" r="41"/>
        <circle cx="776" cy="373" r="41"/>
      </g>
      <g stroke="#ffffff" stroke-width="3" fill="none">
        <circle cx="396" cy="178" r="17"/>
        <path d="M396 168 V178 L404 184"/>
        <rect x="762" y="164" width="18" height="18"/>
        <rect x="772" y="174" width="18" height="18"/>
      </g>
      <g fill="#ffffff">
        <circle cx="396" cy="364" r="6"/><circle cx="384" cy="368" r="5"/><circle cx="408" cy="368" r="5"/>
        <path d="M386 386 a10 10 0 0 1 20 0Z"/><path d="M374 386 a9 9 0 0 1 12 -6 v6Z"/><path d="M418 386 a9 9 0 0 0 -12 -6 v6Z"/>
        <rect x="763" y="378" width="5" height="10"/><rect x="771" y="372" width="5" height="16"/><rect x="779" y="365" width="5" height="23"/><rect x="787" y="358" width="5" height="30"/>
      </g>
    </svg>
    <p class="center-name">Tamrick Holdings</p>
    <p class="value left" style="left:40px;top:148px"><b>RESPONSIVE</b> - Mobile Agility<br>We act and respond swiftly –<br>but responsibly</p>
    <p class="value" style="left:832px;top:160px"><b>TRANSPARENT</b> - we champion our values<br>Connections – leadership – success</p>
    <p class="value left" style="left:40px;top:342px"><b>SUPPORTIVE</b> - welcoming family<br>Considerate and respectful of the<br>importance of lifestyle balance</p>
    <p class="value" style="left:832px;top:352px"><b>PERFORMANCE</b> - network integrity<br>Quality, responsibility and consideration</p>
  </section>

  <section class="message">
    <h2 class="section-title"><span class="title-mark"></span><span>Send a <span class="accent">Message</span></span></h2>
    <div class="field" style="left:222px;top:131px;width:358px;height:44px">Name</div>
    <div class="field" style="left:222px;top:188px;width:358px;height:44px">Email</div>
    <div class="field" style="left:222px;top:245px;width:358px;height:44px">Phone</div>
    <div class="field" style="left:594px;top:131px;width:357px;height:102px">Message</div>
    <div class="send">SEND</div>
  </section>

  <footer class="site-footer">
    <div class="footer-tab"></div>
    <div class="footer-brand"><span class="brand-dot"></span>Tamrick Holdings</div>
    <p class="footer-tagline">people<span class="sep"></span>capital<span class="sep"></span>strategy</p>
    <nav class="footer-nav">
      <span class="is-active">Home</span><span>Who We Are</span><span>What We Do</span><span>What Makes Us Different</span><span>Contact</span>
    </nav>
  </footer>
  <p class="copyright">Copyright © 2017 Tamrick Holdings. All rights reserved.</p>

</div>
</body>
</html>
```